Business card - Brio Margin - size 85 mm * 55 mm

We need new business cards. Design must fit with our vision of the firm. You find in the attached file our logo and a short description of our firm (mission, vision, value, business and so on).

Target Market(s)

Consulting firm in performance improvement

Industry/Entity Type

Management Consulting

Contact Information for Business Card

SIZE
85 mm * 55 mm
INFORMATIONS
name surname
role position
telephone number
email address

Requirements
Must have
• the brand must APPEAR for the rest Would we like to have something sleek, inspired to a "just right" approach
Should not have
• Please avoid the black color as background

```html
<!DOCTYPE html>
<html lang="en">
<head>
<meta charset="utf-8">
<title>Brio Margin – Business Cards</title>
<link rel="stylesheet" href="https://fonts.googleapis.com/css2?family=Exo+2:wght@400;500&display=swap">
<style>
  :root {
    --backdrop: #3a3a3a;
    --card: #444444;
    --accent: #8dc63f;
    --text-light: #f2f2f2;
  }
  * { margin: 0; padding: 0; box-sizing: border-box; }
  html, body { width: 1200px; height: 810px; overflow: hidden; background: var(--backdrop); }
  .canvas {
    position: relative; width: 1200px; height: 810px;
    font-family: "Exo 2", sans-serif;
  }
  .card {
    position: absolute; top: 237px; width: 520px; height: 336px;
    background: var(--card); border-radius: 22px; overflow: hidden;
    box-shadow: 0 6px 18px rgba(0,0,0,0.35);
  }
  .card--front { left: 50px; }
  .card--back { left: 630px; }

  .brand { display: flex; flex-direction: column; align-items: center; }
  .brand__circle {
    width: 70px; height: 70px; border-radius: 50%;
    border: 4px solid var(--accent);
  }
  .brand__name {
    color: var(--accent); font-weight: 500; text-transform: uppercase;
    letter-spacing: 0.55em; margin-right: -0.55em; white-space: nowrap;
  }
  .card--front .brand { margin-top: 92px; }
  .card--front .brand__name { font-size: 30px; margin-top: 26px; }

  .card--back .brand { margin-top: 46px; }
  .card--back .brand__circle { width: 46px; height: 46px; border-width: 3px; }
  .card--back .brand__name { font-size: 19px; margin-top: 14px; }

  .person { text-align: center; margin-top: 10px; }
  .person__name { color: var(--accent); font-size: 19px; font-weight: 500; }
  .person__role { color: var(--text-light); font-size: 13px; margin-top: 2px; }

  .contact { margin: 18px auto 0; width: 260px; font-size: 13px; line-height: 1.55; }
  .contact__label { color: var(--accent); }
  .contact__value { color: var(--text-light); }

  .card__band {
    position: absolute; bottom: 0; left: 130px; width: 300px; height: 36px;
    background: var(--accent); border-radius: 26px 40px 0 0;
  }
</style>
</head>
<body>
<main class="canvas">
  <section class="card card--front" aria-label="Card front">
    <div class="brand">
      <span class="brand__circle"></span>
      <span class="brand__name">Brio Margin</span>
    </div>
  </section>

  <section class="card card--back" aria-label="Card back">
    <div class="brand">
      <span class="brand__circle"></span>
      <span class="brand__name">Brio Margin</span>
    </div>
    <div class="person">
      <p class="person__name">Adrien Coleman</p>
      <p class="person__role">President</p>
    </div>
    <div class="contact">
      <p><span class="contact__label">Phone:</span> <span class="contact__value">0400555218</span></p>
      <p><span class="contact__label">E-mail:</span> <span class="contact__value">Contact@briomargin.com</span></p>
    </div>
    <div class="card__band"></div>
  </section>
</main>
</body>
</html>
```